We need a poster designed for use on facebook, as well as to print out for advertising in local noticeboards and shop windows.
The poster will advertise the Fernhollow Turf Society 30th Anniversary Ball.
the ball will be held on the 28th April 2018 at the Fernhollow Community Hall.
Time will be 630pm till late. Ticket Price is $120 which includes 3 course dinner, drinks on arrival and entertainment during the evening.
Additional details will need to be added to the poster at a later date.
The fernhollow Turf Society is a horse racing club run by the community. The club has been incorporateds for 30 years. This Ball will be a celebration of that anniversary.

Target Market(s)

Middlemount Community

Industry/Entity Type

Club

Font styles to use
Serif
Decorative

Colors
1b1b1b
fbfbfb
6b449b
886aae
a64599
ffc214

Requirements
Must have
• Include
• where when time and cost
• ticket inclusions
• entertainement by Colin Hartwell
Nice to have
• Attached are some images for inspiration.
• It would be nice to have the race club logo included somewhere however not prominant.
Should not have
• Abstract geometriic lines
• images of people
• primary colours

```html
<!DOCTYPE html>
<html lang="en">
<head>
<meta charset="utf-8">
<title>Fernhollow Turf Society 30th Anniversary Ball</title>
<link rel="stylesheet" href="https://fonts.googleapis.com/css2?family=Kaushan+Script&family=Quicksand:wght@600&family=Antic+Didone&display=swap">
<style>
  :root {
    --board: #30312d;
    --board-edge: #262723;
    --gold: #ffc214;
    --brass: #a88a4e;
    --brass-soft: rgba(168, 138, 78, 0.55);
    --white: #fbfbfb;
    --lilac: #886aae;
    --plum: #a64599;
  }
  html, body {
    margin: 0;
    padding: 0;
    overflow: hidden;
    background: var(--board);
  }
  .poster {
    position: relative;
    width: 776px;
    height: 1200px;
    overflow: hidden;
    background: radial-gradient(ellipse at 50% 45%, var(--board) 55%, var(--board-edge) 100%);
    font-family: "Quicksand", sans-serif;
  }
  .flourish {
    position: absolute;
    left: 10px;
    right: 10px;
    height: 56px;
    background: linear-gradient(90deg, var(--brass-soft), rgba(168,138,78,0.12) 30%, rgba(168,138,78,0.12) 70%, var(--brass-soft));
    border-radius: 6px;
  }
  .flourish--top { top: 6px; }
  .flourish--bottom { bottom: 6px; }
  .side-rule {
    position: absolute;
    top: 170px;
    width: 4px;
    height: 876px;
    background: var(--brass);
  }
  .side-rule--left { left: 20px; }
  .side-rule--right { right: 20px; }
  .centered {
    position: absolute;
    left: 0;
    width: 100%;
    margin: 0;
    text-align: center;
  }
  .script {
    font-family: "Kaushan Script", cursive;
    color: var(--white);
    font-style: normal;
  }
  .invite-line { top: 72px; font-size: 24px; }
  .event-title {
    top: 118px;
    font-family: "Quicksand", sans-serif;
    font-weight: 600;
    font-size: 47px;
    line-height: 68px;
    color: var(--gold);
  }
  .club-mark {
    position: absolute;
    left: 228px;
    top: 330px;
    width: 320px;
    height: 360px;
    display: flex;
    flex-direction: column;
    align-items: center;
    justify-content: center;
    gap: 22px;
  }
  .club-mark__dot {
    width: 90px;
    height: 90px;
    border-radius: 50%;
    background: var(--lilac);
  }
  .club-mark__name {
    font-family: "Quicksand", sans-serif;
    font-weight: 600;
    font-size: 26px;
    color: var(--lilac);
    text-align: center;
    line-height: 1.3;
  }
  .date-line { top: 754px; font-size: 24px; }
  .venue {
    top: 796px;
    font-family: "Antic Didone", serif;
    font-size: 36px;
    letter-spacing: 9px;
    color: var(--plum);
  }
  .time-line { top: 846px; font-size: 24px; }
  .ent-label { top: 924px; font-size: 18px; line-height: 28px; }
  .performer {
    top: 986px;
    font-family: "Antic Didone", serif;
    font-size: 36px;
    letter-spacing: 8px;
    color: var(--gold);
  }
  .ticket-line { top: 1058px; font-size: 20px; }
  .ticket-inclusions { top: 1092px; font-size: 15px; color: var(--lilac); }
</style>
</head>
<body>
<main class="poster">
  <div class="flourish flourish--top" role="img" aria-label="Gold scrollwork flourish across the top edge"></div>
  <div class="side-rule side-rule--left"></div>
  <div class="side-rule side-rule--right"></div>

  <p class="centered script invite-line">You are invited to join the</p>
  <h1 class="centered event-title">Fernhollow Turf Society<br>30th Anniversary Ball</h1>

  <div class="club-mark">
    <span class="club-mark__dot"></span>
    <span class="club-mark__name">Fernhollow<br>Turf Society</span>
  </div>

  <p class="centered script date-line">on the 28th April 2018 at the</p>
  <p class="centered venue">Fernhollow Community Hall</p>
  <p class="centered script time-line">at 6:30 in the evening till late</p>

  <p class="centered script ent-label">Entertainement<br>by</p>
  <p class="centered performer">Colin Hartwell</p>

  <p class="centered script ticket-line">Ticket price: $120</p>
  <p class="centered script ticket-inclusions">includes 3 course dinner, drinks on arrival &amp; entertainment</p>

  <div class="flourish flourish--bottom" role="img" aria-label="Gold scrollwork flourish across the bottom edge"></div>
</main>
</body>
</html>
```